Tech Savy small Business accountant business card design

We need a business card for a new company based in the cloud. We provide tax, business advisory, accounting, information technology solutions and back office functions to small businesses. We offer fixed fee packages with add on services as you need them. By harnessing technology we simplify small business operational processes providing valuable time and information for small business owners to grow their business. In the logo (zulvarine) we want to be able to see zulv and experts. The final design should communicate achieving growth dreams and balance (ie life and $).
Updates
This project has been temporarily placed on hold until I finalize "Tech Savy small Business accountant needs a logo". I invite all designers to submit on this logo project. Once my logo is finalized I will resume this business card contest. Thanks Added Wednesday, March 19, 2014
This project has been temporarily placed on hold until I finalize "Tech Savy small Business accountant logo". I invite all designers to submit on this logo project. Once my logo is finalized I will resume this business card contest. Thanks Added Thursday, March 20, 2014
Target Market(s)
Small Business (Revenue $500,000, more than 3 employees) owners.
Industry/Entity Type
Small Business
Contact Information for Business Card
Marla Pennick (Principal)
Accountant, Tax Agent.
TEL | 0417 583 916
EMAIL | Marla.Pennick@zulvarine.com.au
WEB | www.zulvarine.com.au
Look and feel

```html
<!DOCTYPE html>
<html lang="en">
<head>
<meta charset="utf-8">
<title>zulvarine business card</title>
<link rel="stylesheet" href="https://fonts.googleapis.com/css2?family=Roboto:wght@400;500;700&display=swap">
<style>
  :root {
    --backdrop: #c2c2c2;
    --card-white: #ffffff;
    --brand-blue: #5596d6;
    --accent-blue: #5a9bd5;
    --rule-blue: #93b6d3;
    --ink-dark: #4a4a4a;
    --ink-mid: #5c5c5c;
  }
  * { margin: 0; padding: 0; box-sizing: border-box; }
  html, body {
    width: 1200px;
    height: 750px;
    overflow: hidden;
  }
  body {
    background: var(--backdrop);
    font-family: "Roboto", Arial, sans-serif;
    position: relative;
  }
  .card {
    position: absolute;
    top: 236px;
    width: 490px;
    height: 278px;
    border-radius: 20px;
  }
  .card-front {
    left: 99px;
    background: var(--card-white);
  }
  .card-back {
    left: 613px;
    background: var(--brand-blue);
    display: flex;
    align-items: center;
    justify-content: center;
  }
  .brand-block {
    position: absolute;
    left: 36px;
    top: 34px;
  }
  .brand-name {
    font-size: 30px;
    font-weight: 500;
    color: var(--ink-mid);
    letter-spacing: -0.5px;
    line-height: 1;
  }
  .brand-tagline {
    margin-top: 4px;
    font-size: 8.5px;
    color: var(--ink-mid);
    line-height: 1;
  }
  .divider {
    position: absolute;
    left: 35px;
    top: 105px;
    width: 421px;
    height: 1px;
    background: var(--rule-blue);
  }
  .person-name {
    position: absolute;
    left: 35px;
    top: 124px;
    font-size: 21px;
    font-weight: 400;
    color: var(--ink-dark);
    line-height: 1;
  }
  .person-role {
    position: absolute;
    left: 35px;
    top: 152px;
    font-size: 14.5px;
    letter-spacing: 2px;
    color: var(--accent-blue);
    line-height: 1;
  }
  .contact-list {
    position: absolute;
    left: 35px;
    top: 190px;
    list-style: none;
  }
  .contact-item {
    display: flex;
    font-size: 15px;
    line-height: 19.5px;
    color: var(--ink-dark);
  }
  .contact-label {
    width: 22px;
    font-weight: 500;
    color: var(--accent-blue);
  }
  .back-brand {
    font-size: 62px;
    font-weight: 500;
    color: var(--card-white);
    letter-spacing: -1px;
    line-height: 1;
  }
</style>
</head>
<body>
  <section class="card card-front">
    <div class="brand-block">
      <div class="brand-name">zulvarine</div>
      <div class="brand-tagline">Your business and accounting partner</div>
    </div>
    <div class="divider"></div>
    <h1 class="person-name">Marla Pennick</h1>
    <p class="person-role">PRINCIPAL</p>
    <ul class="contact-list">
      <li class="contact-item"><span class="contact-label">T</span><span>0417 583 916</span></li>
      <li class="contact-item"><span class="contact-label">E</span><span>marla.pennick@zulvarine.com.au</span></li>
      <li class="contact-item"><span class="contact-label">W</span><span>www.zulvarine.com.au</span></li>
    </ul>
  </section>
  <section class="card card-back">
    <div class="back-brand">zulvarine</div>
  </section>
</body>
</html>
```